Webdesign für  Kranken- und Seniorenpflege
Webdesign für Kranken- und Seniorenpflege
Zielgruppe
Ambulante Kranken- und Seniorenpflege
Tagespflege in Limbach-Oberfrohna, Mittweida und Chemnitz
Palliativpflege
Aufgabenstellung
- Erstellung in Adobe Photoshop
- Orientieren Sie sich am Socialmedia-Auftritt des Kunden

```html
<!DOCTYPE html>
<html lang="de">
<head>
<meta charset="utf-8">
<title>Sonnenhof Pflege</title>
<link href="https://fonts.googleapis.com/css2?family=Kumbh+Sans:wght@500;600;700&family=Lato:wght@400;700&display=swap" rel="stylesheet">
<style>
:root{
  --brand:#9b0a3f;
  --brand-dark:#870834;
  --pink:#fde7ee;
  --yellow:#fbbf24;
  --ink:#1f1f1f;
  --muted:#6b6b6b;
  --line:#dadada;
  --footer-bar:#eeeeee;
}
*{margin:0;padding:0;box-sizing:border-box}
html,body{width:1200px;height:3324px;overflow:hidden}
body{position:relative;background:#fff;font-family:"Lato",sans-serif;color:var(--ink)}
.abs{position:absolute}
.head-font{font-family:"Kumbh Sans",sans-serif}
.brand-name{font-family:"Lato",sans-serif;font-weight:700;color:var(--brand);font-size:22px;display:flex;align-items:center;gap:10px}
.brand-dot{width:34px;height:34px;border-radius:50%;background:var(--yellow)}
.social{width:22px;height:22px;border-radius:50%;border:2.5px solid var(--ink)}
.phone-pill{background:var(--brand);color:#fff;border-radius:5px;font-size:12px;display:flex;align-items:center;gap:8px;padding:0 12px;height:30px}
.nav{left:0;top:81px;width:1200px;height:34px;background:var(--brand);display:flex;justify-content:space-between;align-items:center;padding:0 93px;color:#fff;font-size:11.5px}
.nav .active{font-weight:700}
.hero{left:0;top:115px;width:1200px;height:526px}
.dots{left:186px;top:395px;display:flex;gap:8px}
.dots span{width:21px;height:2px;background:#fff;opacity:.8}
.hero-title{left:186px;top:410px;color:#fff;font-size:35px;font-weight:700;line-height:47px}
.btn{background:var(--brand);color:#fff;border-radius:5px;font-size:12.5px;font-weight:700;display:flex;align-items:center;justify-content:center;font-family:"Kumbh Sans",sans-serif}
.label{font-size:13px;color:var(--muted);font-family:"Kumbh Sans",sans-serif;font-weight:600}
.h2{color:var(--brand);font-family:"Kumbh Sans",sans-serif;font-weight:700;font-size:31px;line-height:35px}
.rule{width:20px;height:2px;background:var(--ink)}
.center{left:0;width:1200px;text-align:center}
.photo{border-radius:6px}
.card-label{font-size:17px;font-weight:700;color:#333;text-align:center;font-family:"Kumbh Sans",sans-serif}
.news-img{left:266px;width:218px;height:142px;border-radius:3px}
.news-body{left:511px;width:420px}
.tag{display:inline-block;background:var(--brand);color:#fff;font-size:10px;font-weight:700;padding:4px 9px;border-radius:3px;font-family:"Kumbh Sans",sans-serif}
.news-title{font-size:18px;font-weight:600;font-family:"Kumbh Sans",sans-serif;margin:12px 0 10px}
.news-text{font-size:13px;line-height:20px;color:#333}
.cta-title{left:181px;top:2798px;color:#fff;font-size:24px;font-weight:700}
.cta-text{left:181px;top:2840px;width:460px;color:#fff;font-size:11.5px;line-height:20px}
.call{left:758px;top:2800px;color:#fff;font-size:25px;font-weight:700;display:flex;align-items:center;gap:12px}
.foot-head{font-size:13px;font-weight:700;letter-spacing:.3px;color:#333}
.foot-link{font-size:13.5px;color:var(--muted);line-height:26.5px}
</style>
</head>
<body>

<!-- Header -->
<div class="abs brand-name" style="left:98px;top:22px"><span class="brand-dot"></span>Sonnenhof Pflege</div>
<div class="abs social" style="left:908px;top:30px"></div>
<div class="abs social" style="left:948px;top:30px"></div>
<div class="abs phone-pill" style="left:986px;top:26px">
  <svg width="12" height="12" viewBox="0 0 24 24"><path fill="#fff" d="M6.6 10.8a15 15 0 0 0 6.6 6.6l2.2-2.2c.3-.3.7-.4 1-.2 1.1.4 2.3.6 3.6.6.6 0 1 .4 1 1V20c0 .6-.4 1-1 1A17 17 0 0 1 3 4c0-.6.4-1 1-1h3.5c.6 0 1 .4 1 1 0 1.3.2 2.5.6 3.6.1.3 0 .7-.2 1z"/></svg>
  0800 1234567
</div>
<nav class="abs nav">
  <span class="active">Kranken- und Seniorenpflege</span><span>Tagespflege</span><span>Palliativpflege</span><span>Standorte</span><span>Stellenangebote</span><span>Aktuelles</span><span>Impressum / Datenschutz</span>
</nav>

<!-- Hero -->
<svg class="abs hero" viewBox="0 0 1200 526" role="img" aria-label="Foto: Pflegerin und lachende Seniorin im Garten">
  <defs>
    <linearGradient id="heroFill" x1="0" y1="0" x2="1" y2="1">
      <stop offset="0" stop-color="#6f7e5a"/>
      <stop offset=".45" stop-color="#4f6d8f"/>
      <stop offset=".75" stop-color="#c9b9ad"/>
      <stop offset="1" stop-color="#8d8a86"/>
    </linearGradient>
  </defs>
  <path d="M0 0H1200V355C1190 420 1130 440 1000 450C760 470 560 440 390 500C300 530 220 530 0 480Z" fill="url(#heroFill)"/>
  <path d="M0 0H1200V355C1190 420 1130 440 1000 450C760 470 560 440 390 500C300 530 220 530 0 480Z" fill="#000" opacity=".18"/>
</svg>
<div class="abs dots"><span></span><span></span><span></span><span></span></div>
<h1 class="abs hero-title head-font">Herzlich Willkommen bei<br>Sonnenhof Pflege!</h1>
<div class="abs btn" style="left:186px;top:516px;width:143px;height:34px">Mehr enfahren</div>

<!-- Services -->
<div class="abs center label" style="top:703px">Services</div>
<h2 class="abs center h2" style="top:726px">Everyone Deserves Our<br>Best Services</h2>
<div class="abs rule" style="left:590px;top:803px"></div>

<div class="abs photo" style="left:179px;top:844px;width:275px;height:200px;background:linear-gradient(135deg,#8a3a3a,#c7b6a8 60%,#6d6a72)" role="img" aria-label="Foto: Pflegerin mit Seniorin"></div>
<div class="abs photo" style="left:470px;top:844px;width:267px;height:200px;background:linear-gradient(135deg,#f1eeea,#d9b98a 55%,#f4f2ef)" role="img" aria-label="Foto: Brettspiel in der Tagespflege"></div>
<div class="abs photo" style="left:752px;top:844px;width:267px;height:200px;background:linear-gradient(135deg,#e9ebee,#8fa9c9 50%,#f3f1ee)" role="img" aria-label="Foto: Seniorin im Beratungsgespräch"></div>
<div class="abs card-label" style="left:179px;top:1066px;width:310px">Kranken- und Seniorenpflege</div>
<div class="abs card-label" style="left:470px;top:1066px;width:267px">Tagespflege</div>
<div class="abs card-label" style="left:752px;top:1066px;width:267px">Pflegeberatung</div>

<!-- Hiring -->
<svg class="abs" style="left:0;top:1130px" width="1200" height="620" viewBox="0 0 1200 620">
  <path d="M80 82L800 5C900 -5 1000 10 1200 90V430C1190 510 1130 540 1060 540L460 605C400 612 330 620 220 600C120 580 40 550 0 530V160C0 120 40 90 80 82Z" fill="var(--pink)"/>
</svg>
<div class="abs photo" style="left:179px;top:1280px;width:456px;height:318px;background:linear-gradient(135deg,#c9d0d6,#5d6a80 55%,#e0ddd8);box-shadow:0 10px 25px rgba(0,0,0,.18)" role="img" aria-label="Foto: Lächelndes Pflegeteam"></div>
<div class="abs label" style="left:699px;top:1321px">Stellenangebote</div>
<h2 class="abs h2" style="left:699px;top:1346px">We Are Hiring!</h2>
<div class="abs rule" style="left:699px;top:1387px"></div>
<p class="abs news-text" style="left:699px;top:1407px;width:320px">Lorem ipsum dolor sit amet, consectetur adipiscing elit. Volutpat eros, hac massa, eget. Commodo, in tellus lobortis iaculis porttitor nec non faucibus urna. Egestas hendrerit ut purus vitae a nisl, purus nec. Fermentum eget tincidunt vel congue porttitor ornare euismod.</p>
<div class="abs btn" style="left:699px;top:1527px;width:144px;height:33px">Mehr enfahren</div>

<!-- News -->
<div class="abs center label" style="top:1809px">Aktualles</div>
<h2 class="abs center h2" style="top:1832px">Neuesten Nachrichten</h2>
<div class="abs rule" style="left:590px;top:1875px"></div>

<div class="abs news-img" style="top:1914px;background:linear-gradient(135deg,#f1eeea,#d9b98a 55%,#f4f2ef)" role="img" aria-label="Foto: Brettspiel"></div>
<div class="abs news-body" style="top:1916px"><span class="tag">Aktualles</span><div class="news-title">Sommerfest in der Tagespflege „Sonnenblume“</div><p class="news-text">Sommereinklang in der Tagespflege „Sonnenblume“ in Chemnitz. Bei sommerlichen Temperaturen und strahlenden Sonnenschein verweilten die Tagesgäste auf unserer großzügigen Terrasse. Unsere Betreuungskraft Henrike sorgte für …</p></div>

<div class="abs news-img" style="top:2096px;background:linear-gradient(135deg,#e9ebee,#8fa9c9 50%,#f3f1ee)" role="img" aria-label="Foto: Seniorin im Gespräch"></div>
<div class="abs news-body" style="top:2098px"><span class="tag">Aktualles</span><div class="news-title">Wochenausklang am Schwanenteich in Mittweida</div><p class="news-text">Die vergangene Woche haben wir mit unseren Gästen aus der Tagespflege „Kastanienhof“ am Schwanenteich in Mittweida ausklingen lassen. Nach einem Spaziergang durch den Park …</p></div>

<div class="abs news-img" style="top:2278px;background:linear-gradient(135deg,#8a3a3a,#c7b6a8 60%,#6d6a72)" role="img" aria-label="Foto: Pflegerin mit Seniorin"></div>
<div class="abs news-body" style="top:2280px"><span class="tag">Aktualles</span><div class="news-title">Maifest in der Tagespflege „Kastanienhof“</div><p class="news-text">Zu unserem Maifest in der Tagespflege „Kastanienhof“ in Mittweida erlebten unsere Gäste bei schönstem Wetter einen abwechslungsreichen Tag. Mit leckerer Maibowle, Nudelsalat und Bratwurst …</p></div>

<div class="abs news-img" style="top:2460px;background:linear-gradient(135deg,#f1eeea,#d9b98a 55%,#f4f2ef)" role="img" aria-label="Foto: Brettspiel"></div>
<div class="abs news-body" style="top:2462px"><span class="tag">Aktualles</span><div class="news-title">Ostern in unserer Tagespflege „Lindenblick“</div><p class="news-text">Das Osterfest in unserer Tagespflege „Lindenblick“ in Limbach-Oberfrohna war wieder ein gelungenes Fest. Traditionell gab es für unsere Gäste ein leckeres „Osterlamm“ und natürlich …</p></div>

<!-- CTA -->
<svg class="abs" style="left:0;top:2625px" width="1200" height="348" viewBox="0 0 1200 348">
  <path d="M0 60C300 70 700 100 1080 105C1150 100 1185 70 1200 40V348H0Z" fill="var(--brand)"/>
</svg>
<h3 class="abs cta-title head-font">Schedule Your Service Today</h3>
<p class="abs cta-text">Lorem ipsum dolor sit amet, consectetur adipiscing elit. Faucibus sodales et sit egestas tellus venenatis pulvinar. Fermentum nullam morbi vitae lacus sed ullamcorper in leo sit. Ultricies ac enim quam venenatis nibh amet</p>
<div class="abs call head-font">
  <svg width="22" height="22" viewBox="0 0 24 24"><path fill="#fff" d="M6.6 10.8a15 15 0 0 0 6.6 6.6l2.2-2.2c.3-.3.7-.4 1-.2 1.1.4 2.3.6 3.6.6.6 0 1 .4 1 1V20c0 .6-.4 1-1 1A17 17 0 0 1 3 4c0-.6.4-1 1-1h3.5c.6 0 1 .4 1 1 0 1.3.2 2.5.6 3.6.1.3 0 .7-.2 1z"/></svg>
  Call 0800 1234567
</div>
<div class="abs btn" style="left:880px;top:2853px;width:139px;height:37px;background:var(--yellow);color:#fff;font-weight:600">Schedule Service</div>

<!-- Footer -->
<div class="abs brand-name" style="left:186px;top:3040px"><span class="brand-dot"></span>Sonnenhof Pflege</div>
<div class="abs" style="left:181px;top:3098px;font-size:13px">Unsere Hotline hilft Ihnen gerne:</div>
<div class="abs" style="left:181px;top:3124px;font-size:21px;display:flex;align-items:center;gap:10px">
  <svg width="16" height="16" viewBox="0 0 24 24"><path fill="var(--ink)" d="M6.6 10.8a15 15 0 0 0 6.6 6.6l2.2-2.2c.3-.3.7-.4 1-.2 1.1.4 2.3.6 3.6.6.6 0 1 .4 1 1V20c0 .6-.4 1-1 1A17 17 0 0 1 3 4c0-.6.4-1 1-1h3.5c.6 0 1 .4 1 1 0 1.3.2 2.5.6 3.6.1.3 0 .7-.2 1z"/></svg>
  01234 - 5678900
</div>
<div class="abs" style="left:181px;top:3159px;font-size:13px">Mo-Fr, 10:00 - 17:00 Uhr</div>
<div class="abs social" style="left:183px;top:3188px"></div>
<div class="abs social" style="left:223px;top:3188px"></div>

<div class="abs" style="left:546px;top:3027px">
  <div class="foot-head">SERVICE</div>
  <div style="margin-top:16px" class="foot-link">Kranken- und Seniorenpflege<br>Tagespflege<br>Pflegeberatung</div>
</div>
<div class="abs" style="left:838px;top:3027px">
  <div class="foot-head">UNTERNEHMEN</div>
  <div style="margin-top:16px" class="foot-link">Cookie-Einstellungen<br>Impressum<br>AGB<br>Datenschutz</div>
</div>

<div class="abs" style="left:0;top:3264px;width:1200px;height:60px;background:var(--footer-bar)"></div>
<div class="abs" style="left:135px;top:3287px;font-size:12px;color:var(--muted)">© 2022 – sonnenhof-pflege-beispiel.de</div>

</body>
</html>
```